Stylish High End Wedding Videography/Films Website (BDMR)

We need a modern and high-end website look for our wedding video and films business. We films weddings all over the United Kingdom and at European destinations so need something to reflect our work. The website should be visually stunning with images and videos being the focal point as this is what our services are;

I have uploads of some items I like and the features the site needs to have. These have been taken from other websites using standout features.

We need the following pages;

1 - Homepage
2 - Films Index Page
3 - Individual Films Page
4 - Prices / Collection Page
5 - Reviews
6 - Options
7 - About
8 - Contact
9 - Blog Index
10 - Blog Page

All pages must be consistent so have a similar style.

Pages on menu:
Films
Prices
Reviews
Options
About
Contact

We require a responsive look too. Over 90% of our visitors access the website via their mobile devices.

Please use the colours from our logo to incorporate into the website.

Target Market(s)

Wedding Couples

Industry/Entity Type

Wedding Photography

Number of Pages Required

5+ page

Font styles to use
Sans Serif
Script

Requirements
Must have
• The logo must be in the centre of the menu at the top.

Social icons at the bottom of the page.

Use only two fonts including Lore which is supplied
Nice to have
• Different video for each page on the top header. This will play behind the menu.

```html
<!DOCTYPE html>
<html lang="en">
<head>
<meta charset="utf-8">
<title>BDMR Wedding Films</title>
<link href="https://fonts.googleapis.com/css2?family=Montserrat:wght@300;400;500;600&family=Sacramento&display=swap" rel="stylesheet">
<style>
:root{
  --gold:#9a8350;
  --ink:#4a4a4a;
  --muted:#9a9a9a;
  --paper:#ffffff;
  --mist:#f7f7f7;
  --foot:#f0f0f2;
}
*{margin:0;padding:0;box-sizing:border-box}
html,body{width:1200px;height:4431px;overflow:hidden;background:var(--paper)}
body{position:relative;font-family:"Montserrat",sans-serif;color:var(--ink)}
.abs{position:absolute}
.photo{position:absolute;box-shadow:inset 0 0 60px rgba(0,0,0,.28)}

/* hero */
.hero{left:0;top:0;width:1200px;height:543px;box-shadow:inset 0 0 140px rgba(0,0,0,.45);
  background:
    radial-gradient(ellipse 260px 120px at 1020px 250px,rgba(255,236,190,.9),rgba(255,236,190,0) 70%),
    radial-gradient(ellipse 420px 150px at 560px 90px,rgba(255,255,255,.75),rgba(255,255,255,0) 70%),
    radial-gradient(ellipse 300px 90px at 250px 150px,rgba(240,240,235,.6),rgba(240,240,235,0) 70%),
    radial-gradient(ellipse 120px 230px at 600px 300px,rgba(40,35,30,.35),rgba(40,35,30,0) 75%),
    linear-gradient(180deg,#6f7f8e 0%,#a6afb4 22%,#d8cdb4 40%,#e6cf9c 46%,#a98a52 52%,#7a6034 66%,#4e3b1f 84%,#2f2413 100%)}
.nav{top:33px;font-size:8px;letter-spacing:1px;color:#fff;display:flex;gap:24px;font-weight:500}
.nav-left{left:322px}
.nav-right{left:733px}
.brand{left:500px;top:44px;width:200px;text-align:center;color:#fff;font-size:11px;font-weight:600;letter-spacing:2px;display:flex;justify-content:center;align-items:center;gap:7px}
.brand i{display:inline-block;width:7px;height:7px;background:#fff}
.tagline{left:320px;top:279px;width:560px;text-align:center;color:#fff;font-size:7px;letter-spacing:4px;font-weight:600;border-top:1px solid rgba(255,255,255,.7);border-bottom:1px solid rgba(255,255,255,.7);padding:4px 0}
.slides{left:570px;top:521px;color:#fff;font-size:7px;display:flex;gap:12px}
.slides span:first-child{border-bottom:1px solid #fff}

/* intro */
.intro{left:0;top:543px;width:1200px;height:377px;background:var(--mist)}
.intro-title{left:200px;top:598px;width:800px;text-align:center;font-family:"Sacramento",cursive;font-weight:400;font-size:34px;line-height:36px;color:#555}
.intro-title u{text-underline-offset:4px}
.intro-text{left:300px;top:685px;width:600px;text-align:center;font-size:9.5px;line-height:22px;color:var(--muted)}
.rule-v{left:609px;top:772px;width:1px;height:18px;background:var(--gold)}

.gallery .photo{border:1px solid #fff}

.section-title{width:1200px;left:0;text-align:center;font-size:26px;font-weight:300;letter-spacing:1px;color:#777}
.card{background:var(--mist)}
.body-text{font-size:10px;line-height:17px;color:var(--muted)}
.body-text p+p{margin-top:17px}
.dash{height:1px;background:#ccc}

/* quote band */
.band{left:0;top:2247px;width:1200px;height:545px;box-shadow:inset 0 0 160px rgba(0,0,0,.5);
  background:
    radial-gradient(ellipse 120px 260px at 620px 2px,rgba(0,0,0,0),rgba(0,0,0,0)),
    radial-gradient(ellipse 90px 220px at 610px 280px,rgba(240,240,240,.55),rgba(240,240,240,0) 75%),
    linear-gradient(90deg,rgba(15,15,15,.95) 0%,rgba(40,40,40,.6) 22%,rgba(0,0,0,0) 40%),
    linear-gradient(180deg,#c9c9c9 0%,#d6d6d6 30%,#8a8a8a 46%,#3a3a3a 60%,#2a2a2a 80%,#1c1c1c 100%)}
.quote{left:272px;top:2425px;width:656px;text-align:center;font-family:"Sacramento",cursive;font-size:24px;line-height:27px;color:#fff;text-shadow:0 1px 3px rgba(0,0,0,.5)}
.quote-rule{left:588px;top:2663px;width:24px;height:1px;background:#fff}
.diamond{transform:rotate(45deg);border:3px solid #fff}

.style-bg{left:0;top:2792px;width:1200px;height:560px;background:#fafafa}
.style-rule{left:592px;top:2969px;width:16px;height:1px;background:var(--gold)}
.col{font-size:10px;line-height:20px;color:var(--muted);text-align:justify}
.btn{background:var(--gold);color:#fff;font-size:7px;letter-spacing:1px;font-weight:500;display:flex;align-items:center;justify-content:center}

.logo-word{left:500px;top:3860px;width:200px;text-align:center;color:var(--gold);font-size:30px;font-weight:600;letter-spacing:4px}

.footer{left:0;top:4220px;width:1200px;height:211px;background:var(--foot)}
.socials{left:570px;top:4311px;display:flex;gap:4px}
.socials span{width:13px;height:13px;border:1px solid #888}
.legal{left:0;top:4340px;width:1200px;text-align:center;font-size:7px;letter-spacing:.8px;color:#666}
.legal em{font-style:normal;margin:0 8px;color:#aaa}
</style>
</head>
<body>

<header>
  <div class="abs hero" role="img" aria-label="Couple in wedding dress and suit running hand in hand across a sunlit meadow"></div>
  <nav class="abs nav nav-left"><span>FILMS</span><span>PRICES</span><span>REVIEWS</span></nav>
  <div class="abs brand"><i></i>BDMR</div>
  <nav class="abs nav nav-right"><span>OPTIONS</span><span>ABOUT</span><span>CONTACT</span></nav>
  <div class="abs tagline">WEDDING VIDEOGRAPHY · NORTH EAST, UK AND WORLDWIDE FILMS</div>
  <div class="abs slides"><span>1</span><span>2</span><span>3</span><span>4</span></div>
</header>

<section>
  <div class="abs intro"></div>
  <h1 class="abs intro-title">Not just another pretty dress. Your wedding is<br>a personal story that we are there to <u>document.</u></h1>
  <p class="abs intro-text">We believe best results come from telling it like it is. The art happens in recognizing the moments when<br>the setting, subject and mood are in sync and the real story unfolds naturally, without being contrived.</p>
  <div class="abs rule-v"></div>
</section>

<section class="gallery">
  <div class="photo" style="left:100px;top:825px;width:393px;height:167px;background:radial-gradient(ellipse 90px 70px at 270px 100px,rgba(245,235,225,.8),rgba(245,235,225,0) 70%),radial-gradient(ellipse 140px 90px at 80px 50px,rgba(230,160,120,.6),rgba(230,160,120,0) 70%),linear-gradient(135deg,#8a5e4a,#a87c66 45%,#5e4038)" role="img" aria-label="Wedding ceremony in a warmly lit hall"></div>
  <div class="photo" style="left:493px;top:825px;width:214px;height:167px;background:radial-gradient(ellipse 50px 50px at 120px 130px,rgba(240,235,225,.85),rgba(240,235,225,0) 70%),linear-gradient(180deg,#8a8468 0%,#6c6850 45%,#5a5440 100%)" role="img" aria-label="Couple outside a stone castle"></div>
  <div class="photo" style="left:707px;top:825px;width:393px;height:167px;background:radial-gradient(ellipse 160px 110px at 80px 70px,rgba(235,235,232,.9),rgba(235,235,232,0) 70%),radial-gradient(ellipse 110px 90px at 260px 80px,rgba(220,180,160,.6),rgba(220,180,160,0) 70%),linear-gradient(90deg,#bdbab4,#8a8680 55%,#3e3e42)" role="img" aria-label="Bride and groom close together under a veil"></div>
  <div class="photo" style="left:100px;top:992px;width:607px;height:232px;background:radial-gradient(ellipse 120px 60px at 400px 40px,rgba(250,240,220,.8),rgba(250,240,220,0) 70%),radial-gradient(ellipse 90px 110px at 290px 150px,rgba(40,70,130,.8),rgba(40,70,130,0) 75%),radial-gradient(ellipse 90px 100px at 460px 160px,rgba(245,240,235,.85),rgba(245,240,235,0) 70%),linear-gradient(180deg,#b08450 0%,#7a5a3a 40%,#4a3a30 100%)" role="img" aria-label="Guests throwing confetti over the newlyweds"></div>
  <div class="photo" style="left:707px;top:992px;width:393px;height:232px;background:radial-gradient(ellipse 160px 30px at 200px 30px,rgba(235,200,195,.9),rgba(235,200,195,0) 75%),radial-gradient(ellipse 50px 70px at 140px 120px,rgba(250,248,240,.9),rgba(250,248,240,0) 70%),radial-gradient(ellipse 50px 70px at 250px 120px,rgba(250,248,240,.9),rgba(250,248,240,0) 70%),linear-gradient(180deg,#a4b48a 0%,#7fa656 40%,#5f8c38 100%)" role="img" aria-label="Two decorated chairs on a lawn"></div>
  <div class="photo" style="left:100px;top:1224px;width:393px;height:167px;background:radial-gradient(ellipse 50px 70px at 210px 110px,rgba(245,242,238,.95),rgba(245,242,238,0) 70%),radial-gradient(ellipse 30px 60px at 175px 95px,rgba(40,50,70,.7),rgba(40,50,70,0) 75%),linear-gradient(180deg,#e8e2d6 0%,#dcd6ca 38%,#6fa7ad 48%,#8ab8b6 62%,#d6c8ae 78%,#cdbb9c 100%)" role="img" aria-label="Couple on a beach"></div>
  <div class="photo" style="left:493px;top:1224px;width:214px;height:167px;background:radial-gradient(ellipse 70px 60px at 70px 50px,rgba(235,235,210,.95),rgba(235,235,210,0) 75%),radial-gradient(ellipse 60px 90px at 160px 110px,rgba(240,235,228,.9),rgba(240,235,228,0) 70%),linear-gradient(135deg,#a8a88a,#6a7050 60%,#8a8070)" role="img" aria-label="Bridal bouquet close up"></div>
  <div class="photo" style="left:707px;top:1224px;width:393px;height:167px;background:radial-gradient(ellipse 70px 100px at 230px 110px,rgba(30,25,20,.75),rgba(30,25,20,0) 75%),radial-gradient(ellipse 200px 80px at 60px 40px,rgba(255,230,170,.9),rgba(255,230,170,0) 70%),linear-gradient(180deg,#e6cf9a 0%,#c9a86c 40%,#6a5638 75%,#4a3c28 100%)" role="img" aria-label="Couple embracing at sunset"></div>
</section>

<section>
  <h2 class="abs section-title" style="top:1486px">CHI SONO</h2>

  <div class="abs dash" style="left:342px;top:1620px;width:12px"></div>
  <div class="abs body-text" style="left:198px;top:1642px;width:330px">
    <p>Lorem ipsum dolor sit amet, adipiscing elit, sed do eiusmod incididunt labore et dolore magna aliqua. Risus in hendrerit gravida rutrum quisque non tellus orci ac. At erat</p>
    <p>pellentesque adipiscing commodo elit. Leo a diam sollicitudin tempor accumsan in nisl nisi scelerisque eu ultrices vitae auctor.</p>
  </div>
  <div class="abs card" style="left:555px;top:1542px;width:444px;height:304px"></div>
  <div class="photo" style="left:607px;top:1580px;width:347px;height:230px;background:radial-gradient(ellipse 70px 90px at 185px 70px,rgba(60,60,60,.85),rgba(60,60,60,0) 75%),radial-gradient(ellipse 110px 90px at 230px 200px,rgba(40,40,40,.9),rgba(40,40,40,0) 75%),linear-gradient(180deg,#d4d4d4 0%,#e4e4e4 45%,#b0b0b0 60%,#8a8a8a 100%)" role="img" aria-label="Black and white portrait of the filmmaker by the sea"></div>
  <div class="abs dash" style="left:583px;top:1697px;width:50px"></div>

  <div class="abs card" style="left:199px;top:1894px;width:442px;height:303px"></div>
  <div class="photo" style="left:249px;top:1930px;width:348px;height:231px;background:radial-gradient(ellipse 70px 110px at 175px 140px,rgba(240,240,240,.95),rgba(240,240,240,0) 75%),radial-gradient(ellipse 40px 40px at 175px 50px,rgba(90,90,90,.7),rgba(90,90,90,0) 75%),linear-gradient(90deg,#3a3a3a 0%,#8a8a8a 30%,#c8c8c8 50%,#8a8a8a 70%,#2e2e2e 100%)" role="img" aria-label="Black and white portrait of a smiling bride"></div>
  <div class="abs dash" style="left:575px;top:2046px;width:50px"></div>
  <div class="abs dash" style="left:802px;top:1960px;width:12px"></div>
  <div class="abs body-text" style="left:665px;top:1982px;width:332px">
    <p>Lorem ipsum dolor sit amet, adipiscing elit, sed do eiusmod incididunt labore et dolore magna aliqua. Risus in hendrerit gravida rutrum quisque non tellus orci ac. At erat</p>
    <p>pellentesque adipiscing commodo elit. Leo a diam sollicitudin tempor accumsan in nisl nisi scelerisque eu ultrices vitae auctor.</p>
  </div>
</section>

<section>
  <div class="abs band" role="img" aria-label="Black and white scene of a couple on a dark beach below sea cliffs"></div>
  <p class="abs quote">Lorem ipsum dolor sit amet, adipiscing elit, sed do eiusmod incididunt labore et dolore magna aliqua. Risus in hendrerit gravida rutrum quisque non tellus orci ac. At erat pellentesque adipiscing commodo elit. Leo a diam sollicitudin tempor accumsan in nisl nisi scelerisque eu ultrices vitae auctor. Viverra orci sagittis eu volutpat. Volutpat sed cras ornare arcu dui vivamus. Integer vitae justo eget magna fermentum iaculis eu. Erat nam at lectus urna. Ac tortor vitae purus faucibus ornare.</p>
  <div class="abs quote-rule"></div>
</section>

<section>
  <div class="abs style-bg"></div>
  <div class="abs diamond" style="left:565px;top:2750px;width:70px;height:70px;background:radial-gradient(circle at 45% 55%,#f0f0f0,#9a9a9a 60%,#4a4a4a)" role="img" aria-label="Bride and groom portrait"></div>
  <h2 class="abs section-title" style="top:2920px">IL MIO STILE</h2>
  <div class="abs style-rule"></div>
  <p class="abs col" style="left:297px;top:2998px;width:280px">Lorem ipsum dolor sit amet, adipiscing elit, sed do eiusmod incididunt labore et dolore magna aliqua. Risus in hendrerit gravida rutrum quisque non tellus orci ac. At erat pellentesque adipiscing commodo elit. Leo a diam sollicitudin tempor accumsan in nisl nisi scelerisque eu ultrices vitae auctor. Viverra orci sagittis eu volutpat. Volutpat sed cras ornare arcu dui vivamus. Integer vitae justo eget magna fermentum iaculis eu. Erat nam at lectus urna. Ac tortor vitae purus faucibus ornare.</p>
  <p class="abs col" style="left:622px;top:2998px;width:280px">Lorem ipsum dolor sit amet, adipiscing elit, sed do eiusmod incididunt labore et dolore magna aliqua. Risus in hendrerit gravida rutrum quisque non tellus orci ac. At erat pellentesque adipiscing commodo elit. Leo a diam sollicitudin tempor accumsan in nisl nisi scelerisque eu ultrices vitae auctor. Viverra orci sagittis eu volutpat. Volutpat sed cras ornare arcu dui vivamus. Integer vitae justo eget magna fermentum iaculis eu. Erat nam at lectus urna. Ac tortor vitae purus faucibus ornare.</p>
  <div class="abs btn" style="left:540px;top:3230px;width:118px;height:28px">LEARN MORE</div>
</section>

<section>
  <div class="photo" style="left:120px;top:3474px;width:320px;height:232px;background:radial-gradient(ellipse 110px 120px at 110px 100px,rgba(240,210,185,.85),rgba(240,210,185,0) 70%),radial-gradient(ellipse 90px 110px at 240px 130px,rgba(150,110,80,.8),rgba(150,110,80,0) 75%),linear-gradient(135deg,#c8a488,#9a7458 55%,#4a3a30)" role="img" aria-label="Couple sharing a kiss"></div>
  <div class="photo" style="left:440px;top:3474px;width:320px;height:232px;background:radial-gradient(circle at 70px 60px,rgba(255,210,140,.7),rgba(255,210,140,0) 40px),radial-gradient(circle at 160px 40px,rgba(255,215,150,.6),rgba(255,215,150,0) 35px),radial-gradient(circle at 250px 70px,rgba(255,210,140,.7),rgba(255,210,140,0) 40px),radial-gradient(ellipse 80px 120px at 160px 170px,rgba(20,16,14,.85),rgba(20,16,14,0) 75%),linear-gradient(180deg,#5a4432,#3a2c24 55%,#241c18)" role="img" aria-label="Evening reception with string lights"></div>
  <div class="photo" style="left:760px;top:3474px;width:320px;height:232px;background:radial-gradient(ellipse 110px 60px at 120px 175px,rgba(250,248,244,.95),rgba(250,248,244,0) 70%),radial-gradient(ellipse 60px 100px at 230px 130px,rgba(60,70,90,.75),rgba(60,70,90,0) 75%),linear-gradient(180deg,#c4c0b4 0%,#d8d2c4 35%,#9a9a88 60%,#6a6a5a 100%)" role="img" aria-label="Couple seated on a sofa outdoors by the coast"></div>
</section>

<div class="abs logo-word">BDMR</div>

<section>
  <div class="photo" style="left:0;top:4029px;width:150px;height:191px;background:radial-gradient(ellipse 40px 70px at 70px 130px,#f4f4f4,rgba(244,244,244,0) 75%),linear-gradient(180deg,#e4e4e4,#a0a0a0 60%,#5a5a5a)" role="img" aria-label="Couple under a canopy"></div>
  <div class="photo" style="left:150px;top:4029px;width:150px;height:191px;background:radial-gradient(ellipse 50px 60px at 80px 80px,#d8d8d8,rgba(216,216,216,0) 75%),linear-gradient(135deg,#5a5a5a,#9a9a9a 50%,#3a3a3a)" role="img" aria-label="Couple portrait"></div>
  <div class="photo" style="left:300px;top:4029px;width:150px;height:191px;background:radial-gradient(ellipse 50px 70px at 60px 110px,#bcbcbc,rgba(188,188,188,0) 75%),linear-gradient(135deg,#a0a0a0,#6a6a6a 50%,#2e2e2e)" role="img" aria-label="Groom with guests"></div>
  <div class="photo" style="left:450px;top:4029px;width:150px;height:191px;background:radial-gradient(ellipse 50px 70px at 80px 100px,#d0d0d0,rgba(208,208,208,0) 75%),linear-gradient(135deg,#3e3e3e,#8a8a8a 50%,#b8b8b8)" role="img" aria-label="Couple dancing"></div>
  <div class="photo" style="left:600px;top:4029px;width:150px;height:191px;background:radial-gradient(ellipse 50px 70px at 70px 100px,#e0e0e0,rgba(224,224,224,0) 75%),linear-gradient(135deg,#c4c4c4,#7a7a7a 50%,#3a3a3a)" role="img" aria-label="Guests celebrating"></div>
  <div class="photo" style="left:750px;top:4029px;width:150px;height:191px;background:radial-gradient(ellipse 50px 80px at 75px 110px,#ededed,rgba(237,237,237,0) 75%),linear-gradient(180deg,#8a8a8a,#c0c0c0 50%,#6a6a6a)" role="img" aria-label="Smiling bride"></div>
  <div class="photo" style="left:900px;top:4029px;width:150px;height:191px;background:radial-gradient(ellipse 60px 80px at 60px 90px,#e8e8e8,rgba(232,232,232,0) 70%),linear-gradient(135deg,#1e1e1e,#5a5a5a 50%,#2a2a2a)" role="img" aria-label="Couple in silhouette"></div>
  <div class="photo" style="left:1050px;top:4029px;width:150px;height:191px;background:radial-gradient(ellipse 50px 70px at 70px 110px,#d6d6d6,rgba(214,214,214,0) 75%),linear-gradient(180deg,#b8b8b8,#8a8a8a 50%,#4a4a4a)" role="img" aria-label="Couple by the sea"></div>
  <div class="abs diamond" style="left:551px;top:4073px;width:98px;height:98px;background:var(--gold)"></div>
  <div class="abs" style="left:550px;top:4118px;width:100px;text-align:center;color:#fff;font-size:7px;letter-spacing:1px;font-weight:500">LEARN MORE</div>
</section>

<footer>
  <div class="abs footer"></div>
  <div class="abs socials"><span></span><span></span><span></span><span></span></div>
  <p class="abs legal">© COPYRIGHT 2020<em>//</em>TERMS AND POLICY<em>//</em>BDMR WEDDING FILMS</p>
</footer>

</body>
</html>
```